Cloud Software Services Business Needs New Website Design

Our client is looking for a really modern design for their cloud services company. We have a logo, but apart from that, if you read the brief fully and digest the wireframes, we hope you will come up with a really amazing end product.

The design of the website should be professional and trustworthy, it is there to inspire confidence in the services and softwares, as well as emphasising the track record of RMV and relative knowledge and competencies.

Given all the cloud-related communications in the messaging on the site, we will need this in either the imagery or icons in the site so that we can connect the messaging with the service offering.

The brand, being black, gives full range for the designer to present a palette that serves the brand, not forgetting the audience are generally IT decision-makers.

Target Market(s)

Managers and Directors Responsible for IT/Cloud Infrastructure

Industry/Entity Type

IT Technology

Number of Pages Required

5+ page

Font styles to use
Sans Serif

Requirements
Must have
• Initial designs which match the brief and wireframes, focus on the homepage and the winning designer will need to supply the internal pages for the website.
Nice to have
• Clearly considered professional website designs, with consistent design work and branding. If choosing stock imagery, then from PixHarbor Basics please.
Should not have
• Not too much colour, or too consumer/youthful.

```html
<!DOCTYPE html>
<html lang="en">
<head>
<meta charset="utf-8">
<title>RMV – Cloud Services</title>
<link rel="stylesheet" href="https://fonts.googleapis.com/css2?family=Montserrat:wght@300;400;500;600;700;800&display=swap">
<style>
:root{
  --yellow:#ffe000;
  --black:#000;
  --ink:#1b1b1b;
  --text:#444;
  --muted:#666;
  --blue:#1a5fb4;
  --olive:#5a4c00;
  --grey-bg:#f4f4f4;
  --white:#fff;
  --badge:#c9cdd2;
}
*{box-sizing:border-box;margin:0;padding:0}
html,body{width:1200px;height:4878px;overflow:hidden}
body{position:relative;background:var(--white);font-family:"Montserrat",sans-serif;color:var(--ink)}
.abs{position:absolute}
svg{display:block}

/* top bar */
.top-bar{left:0;top:0;width:1200px;height:38px;background:var(--yellow)}
.social-dot{width:12px;height:12px;border-radius:50%;background:var(--black);top:13px}
.top-link{top:0;height:38px;display:flex;align-items:center;gap:8px;font-size:12px;font-weight:500;color:var(--ink)}
.top-divider{top:0;width:1px;height:38px;background:rgba(0,0,0,.35)}

/* hero */
.hero{left:0;top:38px;width:1200px;height:682px;background:var(--black)}
.brand{font-weight:700;color:var(--white);letter-spacing:1px}
.nav{top:80px;color:var(--white);font-size:13px;font-weight:500;transform:translateY(-50%)}
.nav-active{border:2px solid var(--yellow);padding:4px 10px;border-radius:3px}
.btn{display:flex;align-items:center;justify-content:center;gap:6px;border-radius:40px;font-size:12px;font-weight:700;text-transform:uppercase}
.btn-yellow{background:var(--yellow);color:var(--black)}
.btn-black{background:var(--black);color:var(--white)}
.btn-white{background:var(--white);color:var(--black)}
.signup{left:1056px;top:64px;width:84px;height:34px;text-transform:none;font-weight:600;font-size:13px}
.hero-title{left:62px;top:215px;color:var(--white);font-size:44px;line-height:58px;font-weight:400}
.hero-title strong{font-weight:800}
.hero-sub{left:62px;top:331px;color:var(--white);font-size:12px;font-weight:500}
.feature-tile{top:375px;width:135px;height:140px;background:var(--olive);border:2px solid #8a7500;border-radius:10px;color:var(--white);display:flex;flex-direction:column;align-items:center;justify-content:flex-end;padding-bottom:18px;text-align:center;font-size:12px;font-weight:500;line-height:18px}
.feature-tile svg{margin-bottom:14px}
.hero-art{left:464px;top:160px;width:681px;height:446px;border-radius:40px 40px 0 0;background:radial-gradient(circle at 30% 55%,#ffe000 0 18%,transparent 19%),linear-gradient(135deg,#2a2a2a,#3b3b3b 60%,#1a1a1a)}

/* intro */
.monitor-art{left:70px;top:852px;width:435px;height:454px;border-radius:14px;background:linear-gradient(180deg,#2d2d2d 0 62%,#d9d9d9 62%,#f0f0f0)}
.intro-title{left:608px;top:846px;font-size:31px;line-height:42px;font-weight:400;color:var(--ink)}
.intro-title strong{color:var(--blue);font-weight:800}
.copy{font-size:12.5px;line-height:22px;color:var(--text)}
.blue{color:var(--blue)}
.intro-list{list-style:none}
.intro-list li{margin-bottom:9px}

/* tools */
.tools-title{left:70px;top:1550px;font-size:29px;font-weight:800}
.tools-sub{left:70px;top:1604px;font-size:14px;font-weight:500}
.tools-art{left:625px;top:1391px;width:492px;height:474px;border-radius:240px 240px 0 0;background:radial-gradient(circle at 50% 60%,#9aa3ad,#d5d9de 60%,#fff 61%)}
.tools-ring{left:640px;top:1395px;width:460px;height:460px;border:2px solid var(--yellow);border-radius:50%}

/* move */
.move-band{left:0;top:1865px;width:1200px;height:587px;background:var(--grey-bg)}
.section-title{left:0;width:1200px;text-align:center;font-size:29px;font-weight:400}
.section-title strong{font-weight:800}
.section-sub{left:0;width:1200px;text-align:center;font-size:12px;line-height:21px;color:var(--muted)}
.provider{width:84px;height:84px;border-radius:50%;background:var(--white);box-shadow:0 6px 18px rgba(0,0,0,.08);display:flex;align-items:center;justify-content:center}
.provider i{display:block;width:34px;height:34px;border-radius:50%;background:var(--badge)}
.dot-grid{background-image:radial-gradient(#cfcfcf 2px,transparent 2.5px);background-size:18px 18px}

/* cost card */
.cost-card{left:114px;top:2285px;width:974px;height:545px;background:var(--white);border-radius:8px;box-shadow:0 10px 40px rgba(0,0,0,.08)}
.cost-badge{left:153px;top:2419px;width:284px;height:263px;background:var(--yellow);border-radius:6px}
.cost-copy{left:479px;top:2419px;width:568px;height:263px;background:var(--white);border-radius:6px;box-shadow:0 6px 26px rgba(0,0,0,.09);padding:48px 40px 0 47px}
.cost-copy p+p{margin-top:22px}

/* start */
.start{left:0;top:2990px;width:1200px;height:465px;background:var(--yellow);overflow:hidden}
.start-mark{left:0;top:30px;width:1200px;text-align:center;font-size:230px;font-weight:700;color:rgba(0,0,0,.05);letter-spacing:6px}
.start-title{left:0;top:3100px;width:1200px;text-align:center;font-size:44px;line-height:56px;font-weight:300}
.start-title strong{display:block;font-weight:800;font-size:46px}

/* partners */
.partners{left:0;top:3455px;width:1200px;height:340px;background:var(--grey-bg)}
.partner{top:3612px;width:201px;height:130px;background:var(--white);display:flex;align-items:center;justify-content:center;gap:8px;font-size:20px;font-weight:500;color:#555}
.partner i{display:block;width:16px;height:16px;background:#888}

/* blog */
.post-img{top:3979px;height:233px;width:340px}
.post-date{top:3979px;width:53px;height:53px;background:var(--yellow);color:var(--white);font-size:11px;line-height:14px;font-weight:600;padding:8px 0 0 12px}
.post-title{top:4232px;font-size:16px;font-weight:700}
.post-text{top:4262px;width:330px;font-size:12px;line-height:22px;color:var(--muted)}
.read-more{top:4322px;font-size:14px;font-weight:500;color:var(--yellow)}

/* footer */
.footer{left:0;top:4540px;width:1200px;height:310px;background:var(--black)}
.foot-head{top:4592px;color:var(--white);font-size:15px;font-weight:600}
.foot-head::after{content:"";display:block;width:38px;height:2px;background:var(--yellow);margin-top:6px}
.foot-links{top:4632px;list-style:none;color:var(--white);font-size:12px;line-height:28px}
.foot-contact{color:var(--white);font-size:12px;display:flex;align-items:center;gap:12px}
.copyright{left:0;top:4850px;width:1200px;height:28px;background:var(--yellow);text-align:center;font-size:11px;line-height:28px;font-weight:500}
.foot-social{top:4750px;width:30px;height:30px;border-radius:50%}
</style>
</head>
<body>

<!-- Top bar -->
<div class="abs top-bar"></div>
<span class="abs social-dot" style="left:56px"></span>
<span class="abs social-dot" style="left:80px"></span>
<span class="abs social-dot" style="left:106px"></span>
<div class="abs top-link" style="left:716px">
  <svg width="20" height="18" viewBox="0 0 20 18"><path d="M3 10a7 7 0 0 1 14 0" fill="none" stroke="#000" stroke-width="2"/><rect x="1" y="9" width="4" height="6" rx="1"/><rect x="15" y="9" width="4" height="6" rx="1"/></svg>
  Customer Support
</div>
<span class="abs top-divider" style="left:880px"></span>
<div class="abs top-link" style="left:913px">Contact</div>
<span class="abs top-divider" style="left:993px"></span>
<div class="abs top-link" style="left:1018px;font-weight:700">
  <svg width="16" height="16" viewBox="0 0 24 24"><path d="M6.6 10.8a15 15 0 0 0 6.6 6.6l2.2-2.2a1 1 0 0 1 1-.25 11.4 11.4 0 0 0 3.6.6 1 1 0 0 1 1 1V20a1 1 0 0 1-1 1A17 17 0 0 1 3 4a1 1 0 0 1 1-1h3.5a1 1 0 0 1 1 1 11.4 11.4 0 0 0 .6 3.6 1 1 0 0 1-.25 1z"/></svg>
  123 456 7890
</div>

<!-- Hero -->
<section class="abs hero"></section>
<div class="abs hero-art" role="img" aria-label="Illustration of two people working with laptops beside a large yellow brand mark and a gear"></div>
<svg class="abs" style="left:0;top:600px" width="1200" height="122" viewBox="0 0 1200 122"><path d="M0 90C120 20 260 30 400 70S700 120 900 60 1130 10 1200 30V122H0Z" fill="#fff"/></svg>

<div class="abs brand" style="left:60px;top:58px;font-size:38px">RMV</div>
<nav>
  <span class="abs nav nav-active" style="left:352px">Home</span>
  <span class="abs nav" style="left:441px">Cloud</span>
  <span class="abs nav" style="left:520px">Services</span>
  <span class="abs nav" style="left:610px">Software</span>
  <span class="abs nav" style="left:707px">Blog</span>
  <span class="abs nav" style="left:778px">Contact Us</span>
</nav>
<a class="abs btn btn-yellow signup">Sign Up</a>

<h1 class="abs hero-title">OPERATING<br><strong>UNDER A CLOUD ?</strong></h1>
<p class="abs hero-sub">THERE'S A SILVER LINING</p>

<div class="abs feature-tile" style="left:60px">
  <svg width="48" height="42" viewBox="0 0 48 42" fill="none" stroke="#fff" stroke-width="2"><path d="M4 6l10 10 8-6 14 12"/><rect x="14" y="24" width="7" height="16"/><rect x="25" y="28" width="7" height="12"/><rect x="36" y="32" width="7" height="8"/></svg>
  REDUCING<br>COST
</div>
<div class="abs feature-tile" style="left:203px">
  <svg width="48" height="42" viewBox="0 0 48 42" fill="none" stroke="#fff" stroke-width="2"><path d="M16 12a8 8 0 0 1 16 0"/><rect x="8" y="22" width="12" height="12"/><rect x="28" y="22" width="12" height="12"/><path d="M24 4v14M20 14l4 4 4-4"/><path d="M4 40h40"/></svg>
  MIGRATION
</div>
<div class="abs feature-tile" style="left:345px">
  <svg width="52" height="42" viewBox="0 0 52 42" fill="none" stroke="#fff" stroke-width="2"><path d="M2 12l10-4 10 6 10-6 10 4 8 2"/><path d="M12 8l-6 16 14 12 16-10-12-10"/><path d="M20 20l6 6M24 16l8 8"/></svg>
  WORK<br>WITH US
</div>

<!-- Intro -->
<div class="abs monitor-art" role="img" aria-label="Desktop computer with keyboard and mouse showing a cloud dashboard"></div>
<h2 class="abs intro-title">DID THE PROMISE OF CLOUD<br><strong>COMPUTING HAPPEN FOR YOU?</strong></h2>
<p class="abs copy" style="left:614px;top:947px;width:540px;font-size:11.5px">We didn't think so! You're not alone. There are may companies just like you who believed in the promise of cloud computing &nbsp;but are now shackled by it.</p>
<p class="abs copy blue" style="left:612px;top:1002px;font-size:12px">But there is a silver lining, reduce costs and simplify their operationas a result.</p>
<p class="abs copy" style="left:612px;top:1043px;width:340px;font-size:13px">It can besummarised in threee promises RMV makes to every client or Partner:</p>
<ol class="abs copy intro-list" style="left:616px;top:1116px;font-size:11.5px">
  <li>1. You can <span class="blue">reduce cloud cost.</span> Without needing to move supplier</li>
  <li>2. You can <span class="blue">migrate</span> from one cloud to another more easily</li>
  <li>3. You can <span class="blue">simplify.</span> your cloud management and choose your favoured provider</li>
</ol>
<p class="abs copy blue" style="left:618px;top:1219px;font-size:13px">If you already know or want to talk to just call</p>
<a class="abs btn btn-yellow" style="left:609px;top:1265px;width:152px;height:37px">
  <svg width="13" height="13" viewBox="0 0 24 24"><path d="M6.6 10.8a15 15 0 0 0 6.6 6.6l2.2-2.2a1 1 0 0 1 1-.25 11.4 11.4 0 0 0 3.6.6 1 1 0 0 1 1 1V20a1 1 0 0 1-1 1A17 17 0 0 1 3 4a1 1 0 0 1 1-1h3.5a1 1 0 0 1 1 1 11.4 11.4 0 0 0 .6 3.6 1 1 0 0 1-.25 1z"/></svg>01632 960 418</a>
<a class="abs btn btn-black" style="left:778px;top:1265px;width:144px;height:37px">Send an email</a>

<!-- Tools -->
<h2 class="abs tools-title">YOUR CLOUD, YOUR TOOLS</h2>
<p class="abs tools-sub">A Suite Of Software to Simplify Deployment</p>
<a class="abs btn btn-yellow" style="left:70px;top:1647px;width:161px;height:34px;font-weight:600">Cloud software</a>
<div class="abs tools-ring"></div>
<div class="abs tools-art" role="img" aria-label="Photo of a smiling man with glasses holding a laptop"></div>
<span class="abs provider" style="left:710px;top:1405px;width:76px;height:76px"><i></i></span>
<span class="abs provider" style="left:917px;top:1403px;width:76px;height:76px"><i></i></span>
<span class="abs provider" style="left:625px;top:1540px;width:76px;height:76px"><i></i></span>
<span class="abs provider" style="left:995px;top:1537px;width:76px;height:76px"><i></i></span>

<!-- Move -->
<section class="abs move-band"></section>
<h2 class="abs section-title" style="top:1935px">HOW HARD IS IT TO <strong>MOVE YOUR CLOUD?</strong></h2>
<p class="abs section-sub" style="top:1991px">Lorem Ipsum is simply dummy text of the printing and typesetting industry. Lorem<br>Ipsum has been the industry's standard dummy text.</p>
<svg class="abs" style="left:160px;top:2060px" width="880" height="100" viewBox="0 0 880 100"><path d="M0 20C100 20 150 80 220 70S360 30 430 30 580 90 650 80 780 20 860 20" fill="none" stroke="#e4e4e4" stroke-width="2"/></svg>
<span class="abs provider" style="left:126px;top:2031px"><i></i></span>
<span class="abs provider" style="left:337px;top:2091px"><i></i></span>
<span class="abs provider" style="left:550px;top:2055px"><i></i></span>
<span class="abs provider" style="left:766px;top:2105px"><i></i></span>
<span class="abs provider" style="left:969px;top:2042px"><i></i></span>
<div class="abs dot-grid" style="left:1046px;top:2220px;width:92px;height:92px"></div>

<!-- Cost card -->
<div class="abs cost-card"></div>
<h2 class="abs section-title" style="top:2331px">MAKE YOUR CLOUD <strong>COSTS EVAPORATE</strong></h2>
<div class="abs cost-badge"></div>
<svg class="abs" style="left:209px;top:2448px" width="188" height="188" viewBox="0 0 188 188"><circle cx="94" cy="94" r="86" fill="none" stroke="#000" stroke-width="6" stroke-dasharray="470 70" transform="rotate(-70 94 94)"/></svg>
<div class="abs" style="left:153px;top:2508px;width:300px;text-align:center;font-size:46px;font-weight:800;line-height:46px">20%</div>
<div class="abs" style="left:153px;top:2558px;width:300px;text-align:center;font-size:20px;font-weight:500">CHEAPER</div>
<div class="abs cost-copy copy" style="font-size:14px;line-height:27px">
  <p>As cloud costs continue to escalate, and as you suddenly hit new tiers of spend, you may feel helpless in the face of rising costs.</p>
  <p>However, even taking the cost of moving into account, RMV has estimated the average client will save 20% of spend on their cloud by using us to find the best solution and help you to move there.</p>
</div>
<a class="abs btn btn-yellow" style="left:526px;top:2730px;width:163px;height:34px;font-weight:600">See case studies</a>
<div class="abs dot-grid" style="left:66px;top:2754px;width:36px;height:72px"></div>
<div class="abs dot-grid" style="left:66px;top:2826px;width:100px;height:18px"></div>

<!-- Get started -->
<svg class="abs" style="left:0;top:2900px" width="1200" height="92" viewBox="0 0 1200 92"><path d="M0 60C150 40 260 -10 420 10S700 70 880 80 1100 60 1200 50V92H0Z" fill="#ffe000"/></svg>
<section class="abs start"><div class="abs start-mark">RMV</div></section>
<h2 class="abs start-title">LET'S<strong>GET STARTED</strong></h2>
<p class="abs copy" style="left:0;top:3238px;width:1200px;text-align:center;font-size:14px;line-height:27px;color:var(--ink)">If You would like to speak to a friendly and helpful member of our team, ask<br>question, discuss option or to help with anything on your mind, please get in touch.</p>
<a class="abs btn btn-white" style="left:458px;top:3320px;width:150px;height:35px">
  <svg width="13" height="13" viewBox="0 0 24 24"><path d="M6.6 10.8a15 15 0 0 0 6.6 6.6l2.2-2.2a1 1 0 0 1 1-.25 11.4 11.4 0 0 0 3.6.6 1 1 0 0 1 1 1V20a1 1 0 0 1-1 1A17 17 0 0 1 3 4a1 1 0 0 1 1-1h3.5a1 1 0 0 1 1 1 11.4 11.4 0 0 0 .6 3.6 1 1 0 0 1-.25 1z"/></svg>01632 960 418</a>
<a class="abs btn btn-black" style="left:627px;top:3320px;width:142px;height:35px">Send an email</a>

<!-- Partners -->
<section class="abs partners"></section>
<h2 class="abs section-title" style="top:3503px">Our Trusted <strong>Partners</strong></h2>
<p class="abs section-sub" style="top:3547px">Lorem Ipsum is simply dummy text of the printing and typesetting industry. Lorem<br>Ipsum has been the industry's standard dummy text.</p>
<div class="abs partner" style="left:60px"><i></i>Vantora</div>
<div class="abs partner" style="left:280px;font-size:17px">Calvenor Lending</div>
<div class="abs partner" style="left:500px"><i style="border-radius:50%"></i>Orbelis</div>
<div class="abs partner" style="left:719px">Nortavel</div>
<div class="abs partner" style="left:939px;font-size:17px">Quellmoor Bank</div>

<!-- Blog -->
<h2 class="abs section-title" style="top:3872px"><strong>Our</strong> Latest Blog</h2>
<p class="abs section-sub" style="top:3914px">Lorem Ipsum is simply dummy text of the printing and typesetting industry. Lorem<br>Ipsum has been the industry's standard dummy text.</p>

<div class="abs post-img" style="left:60px;background:linear-gradient(135deg,#0a2a3a,#1f6f8b 50%,#061a26)" role="img" aria-label="Photo of an engineer with a laptop in a server room"></div>
<div class="abs post-date" style="left:60px">15<br>Jun</div>
<h3 class="abs post-title" style="left:60px">Lorem Ipsum is simply dummy text.</h3>
<p class="abs post-text" style="left:60px">Lorem Ipsum is simply dummy text of the printing and typesetting industry.</p>
<a class="abs read-more" style="left:60px">Read more</a>

<div class="abs post-img" style="left:430px;width:339px;background:radial-gradient(circle at 50% 45%,#3fa8d8,#0b2437 45%,#02070d)" role="img" aria-label="Photo of hands holding a phone with a glowing cloud icon above it"></div>
<div class="abs post-date" style="left:430px">15<br>Aug</div>
<h3 class="abs post-title" style="left:430px">Lorem Ipsum is simply dummy text.</h3>
<p class="abs post-text" style="left:430px">Lorem Ipsum is simply dummy text of the printing and typesetting industry.</p>
<a class="abs read-more" style="left:430px">Read More</a>

<div class="abs post-img" style="left:801px;background:linear-gradient(135deg,#1c2a44,#4d6a8f 55%,#141d2e)" role="img" aria-label="Photo of two colleagues working at a computer in an office"></div>
<div class="abs post-date" style="left:801px">15<br>sep</div>
<h3 class="abs post-title" style="left:801px">Lorem Ipsum is simply dummy text.</h3>
<p class="abs post-text" style="left:801px">Lorem Ipsum is simply dummy text of the printing and typesetting industry.</p>
<a class="abs read-more" style="left:801px">Read More</a>

<!-- Footer -->
<svg class="abs" style="left:0;top:4420px" width="1200" height="122" viewBox="0 0 1200 122"><path d="M0 50C100 20 220 30 360 70S640 110 820 60 1100 10 1200 30V122H0Z" fill="#000"/></svg>
<footer class="abs footer"></footer>
<div class="abs brand" style="left:60px;top:4620px;font-size:80px">RMV</div>
<span class="abs foot-social" style="left:60px;background:var(--white)"></span>
<span class="abs foot-social" style="left:100px;background:var(--yellow)"></span>
<span class="abs foot-social" style="left:141px;background:var(--white)"></span>

<h4 class="abs foot-head" style="left:339px">Quick Links</h4>
<ul class="abs foot-links" style="left:339px">
  <li>Home</li><li>Cloud</li><li>Services</li><li>Software</li><li>Blog</li><li>Contact Us</li>
</ul>
<h4 class="abs foot-head" style="left:613px">Company</h4>
<ul class="abs foot-links" style="left:613px">
  <li>terms of use</li><li>Privacy and Cookies Policy</li>
</ul>
<h4 class="abs foot-head" style="left:891px">Contact Us</h4>
<div class="abs foot-contact" style="left:891px;top:4630px">
  <svg width="16" height="18" viewBox="0 0 16 18" fill="none" stroke="#ffe000" stroke-width="1.6"><path d="M8 17s6-6 6-10A6 6 0 0 0 2 7c0 4 6 10 6 10z"/><circle cx="8" cy="7" r="2"/></svg>
  123 Lorem Ipsum is a dummy text.
</div>
<div class="abs foot-contact" style="left:891px;top:4668px;font-weight:600">
  <svg width="16" height="16" viewBox="0 0 24 24" fill="none" stroke="#ffe000" stroke-width="2"><path d="M6.6 10.8a15 15 0 0 0 6.6 6.6l2.2-2.2a1 1 0 0 1 1-.25 11.4 11.4 0 0 0 3.6.6 1 1 0 0 1 1 1V20a1 1 0 0 1-1 1A17 17 0 0 1 3 4a1 1 0 0 1 1-1h3.5a1 1 0 0 1 1 1 11.4 11.4 0 0 0 .6 3.6 1 1 0 0 1-.25 1z"/></svg>
  123 456 7890
</div>
<div class="abs foot-contact" style="left:891px;top:4708px">
  <svg width="18" height="14" viewBox="0 0 18 14" fill="none" stroke="#ffe000" stroke-width="1.6"><rect x="1" y="1" width="16" height="12"/><path d="M1 1l8 7 8-7"/></svg>
  info@RMV.com
</div>
<div class="abs copyright">Copyright © &nbsp;2022 Nimbrel Systems.All rights reserved.</div>

</body>
</html>
```